American cannabis tech company business card design

Thrum.com is seeking a modern, professional, and brand-aligned business card that represents our company and its core values: Mission, Story, Values, and Impact. As an innovative cannabis company, we want a business card that is not only visually appealing but also serves as a representation of who we are and what we stand for.

Project Scope: Design a double-sided business card that integrates our brand identity and core values. Incorporate our key brand elements, ensuring a sleek and contemporary aesthetic. Visually reflect our core values (Mission, Story, Values, Impact) in a way that is engaging yet professional.

Target Market(s)

Vendors, third parties,

Contact Information for Business Card

Contact details (name, title, email, phone, website, etc.)

Font styles to use
Other font styles liked:
• Caslon, Centra

Colors

Designer to choose colors to be used in the design.

Requirements
Must have
• Thrum.com logo and branding A creative yet clean way to integrate our core values (Mission, Story, Values, Impact) Modern typography and a well-structured layout
Nice to have
• forest green, grey, white, black
Should not have
• references to marijuana, leafs, plants, or related product

```html
<!DOCTYPE html>
<html lang="en">
<head>
<meta charset="utf-8">
<title>Thrum.com Business Card</title>
<link href="https://fonts.googleapis.com/css2?family=Poppins:wght@400;600;700;800&display=swap" rel="stylesheet">
<style>
  :root {
    --backdrop: #2a2a2a;
    --card-light: #efefef;
    --card-light-edge: #e4e4e4;
    --forest: #1f4a26;
    --forest-ink: #143018;
    --ink: #1d1d1d;
    --paper: #ffffff;
  }
  * { box-sizing: border-box; margin: 0; padding: 0; }
  html, body { width: 1200px; height: 1200px; overflow: hidden; }
  body {
    background: var(--backdrop);
    font-family: "Poppins", sans-serif;
    position: relative;
  }
  .card {
    position: absolute;
    left: 201px;
    width: 797px;
    height: 454px;
    border-radius: 19px;
    overflow: hidden;
  }
  .card-front {
    top: 97px;
    background: linear-gradient(160deg, var(--card-light) 0%, var(--card-light-edge) 100%);
  }
  .card-back {
    top: 657px;
    background: var(--forest);
    color: var(--paper);
  }

  /* Front */
  .brand-name {
    position: absolute;
    left: 70px; top: 285px;
    width: 284px;
    text-align: center;
    transform: translateY(-50%);
    position: absolute;
    top: 225px;
    font-weight: 800;
    font-size: 64px;
    letter-spacing: 1px;
    color: var(--forest-ink);
    line-height: 1;
  }
  .divider {
    position: absolute;
    left: 393px; top: 141px;
    width: 2px; height: 170px;
    background: var(--forest-ink);
  }
  .person-name {
    position: absolute;
    left: 436px; top: 135px;
    font-weight: 700;
    font-size: 33px;
    letter-spacing: 0.8px;
    color: var(--forest-ink);
    line-height: 1.2;
  }
  .person-title {
    position: absolute;
    left: 436px; top: 175px;
    font-weight: 400;
    font-size: 22px;
    letter-spacing: 0.6px;
    color: var(--ink);
  }
  .contact-list {
    position: absolute;
    left: 438px; top: 221px;
    list-style: none;
  }
  .contact-item {
    display: flex;
    align-items: center;
    height: 32px;
    font-size: 19px;
    letter-spacing: 0.8px;
    color: var(--ink);
  }
  .contact-icon {
    width: 18px; height: 18px;
    margin-right: 18px;
    flex: none;
  }

  /* Back */
  .intro-heading {
    position: absolute;
    left: 37px; top: 30px;
    font-weight: 800;
    font-size: 23.5px;
    letter-spacing: 0.1px;
    line-height: 1.2;
    padding-bottom: 1px;
    border-bottom: 1.5px solid var(--paper);
  }
  .intro-text {
    position: absolute;
    left: 37px; top: 70px;
    width: 730px;
    font-weight: 700;
    font-size: 16.6px;
    line-height: 21.3px;
    text-transform: uppercase;
  }
  .pillar {
    position: absolute;
    width: 340px;
  }
  .pillar-heading {
    display: inline-block;
    font-weight: 800;
    font-size: 18px;
    line-height: 1.2;
    border-bottom: 1.5px solid var(--paper);
    padding-bottom: 2px;
    margin-bottom: 6px;
  }
  .pillar-text {
    font-size: 12.9px;
    line-height: 15.6px;
    font-weight: 400;
  }
  .pillar-mission { left: 39px; top: 166px; }
  .pillar-story   { left: 39px; top: 279px; }
  .pillar-values  { left: 401px; top: 166px; width: 365px; }
  .pillar-values .pillar-heading { margin-bottom: 3px; }
  .pillar-impact  { left: 401px; top: 291px; width: 365px; }
</style>
</head>
<body>

<section class="card card-front" aria-label="Business card front">
  <div class="brand-name">THRUM</div>
  <div class="divider"></div>
  <h1 class="person-name">DANIEL HAYES</h1>
  <p class="person-title">Co-founder &amp; CEO</p>
  <ul class="contact-list">
    <li class="contact-item">
      <svg class="contact-icon" viewBox="0 0 24 24" fill="none" stroke="#143018" stroke-width="2" stroke-linecap="round" stroke-linejoin="round" aria-hidden="true">
        <path d="M22 16.9v3a2 2 0 0 1-2.2 2 19.8 19.8 0 0 1-8.6-3.1 19.5 19.5 0 0 1-6-6A19.8 19.8 0 0 1 2.1 4.2 2 2 0 0 1 4.1 2h3a2 2 0 0 1 2 1.7c.1 1 .4 1.9.7 2.8a2 2 0 0 1-.5 2.1L8 9.9a16 16 0 0 0 6 6l1.3-1.3a2 2 0 0 1 2.1-.4c.9.3 1.8.6 2.8.7a2 2 0 0 1 1.7 2z"/>
        <path d="M15 2a7 7 0 0 1 7 7M15 6a3 3 0 0 1 3 3"/>
      </svg>
      +1 555-012-4830
    </li>
    <li class="contact-item">
      <svg class="contact-icon" viewBox="0 0 24 24" aria-hidden="true">
        <rect x="2" y="5" width="20" height="14" rx="1" fill="#143018"/>
        <path d="M3 6l9 7 9-7" fill="none" stroke="#efefef" stroke-width="1.8"/>
      </svg>
      team@thrum.com
    </li>
    <li class="contact-item">
      <svg class="contact-icon" viewBox="0 0 24 24" fill="none" stroke="#143018" stroke-width="2" aria-hidden="true">
        <circle cx="12" cy="12" r="10"/>
        <path d="M2 12h20M12 2a15 15 0 0 1 0 20M12 2a15 15 0 0 0 0 20"/>
      </svg>
      thrum.com
    </li>
  </ul>
</section>

<section class="card card-back" aria-label="Business card back">
  <h2 class="intro-heading">WHO WE ARE, AND WHAT WE STAND FOR</h2>
  <p class="intro-text">We believe that everyone’s got different moods, and improving yours should be easy. That’s why we created Thrum, an online source for 100% federally legal cannabis from America’s favorite farms, that helps you quickly and easily get to your best mood.</p>

  <div class="pillar pillar-mission">
    <h3 class="pillar-heading">MISSION</h3>
    <p class="pillar-text">We think cannabis should be accessible, affordable, convenient, and transparent. But most importantly, we believe in supporting the American farmers who make all of this possible.</p>
  </div>

  <div class="pillar pillar-story">
    <h3 class="pillar-heading">STORY</h3>
    <p class="pillar-text">Founded in 2022 by Daniel Hayes and Owen Marsh, Thrum now has a global team of 200+ full-time employees in addition to our robust network of small, U.S. farmers and manufacturing partners. We've built partnerships with over 50 small American farms, bolstering local economies and promoting sustainable farming practices.</p>
  </div>

  <div class="pillar pillar-values">
    <h3 class="pillar-heading">VALUES</h3>
    <p class="pillar-text">At our core is a commitment to product quality and world-class customer experiences. Our company culture fosters open communication &amp; open doors: everybody here has a voice, &amp; we believe that by in-vesting in both our people &amp; our customers, we all will rise.</p>
  </div>

  <div class="pillar pillar-impact">
    <h3 class="pillar-heading">IMPACT</h3>
    <p class="pillar-text">Social impact is a business pillar, not an afterthought. This year, we've donated tens of thousands of dollars to pet humane societies. We’ve contributed to the campaigns of politicians who advocate for cannabis, contributing to the broader movement toward recognition and acceptance.</p>
  </div>
</section>

</body>
</html>
```